Dentistry Office

We want a new design for a Dentist's office website.

The theme is: "We provide high quality, state-of-the-art, dental care in a comfortable, caring environment."

The site currently has a menu on the left of the page with about 40 items on it. There is a great deal of textual content on each page, plus several illustrations.

We want to do this using CSS, so we need specifications in the CSS for all possible elements. The CSS needs to be named in a logical manner for easy use.

Every dentist on the planet seems to use lots of Flash. We don't want to because it is so distracting. We are looking for an elegant solution targeting 24-55 age group, but not excluding anyone.

The following (from another dentist's site) can give you a taste of what we want to communicate on the site:

"After 20 years of teaching dentists how to refine their technique and many years of writing textbooks, I currently devote my time to my office and the hands-on practice of dentistry. I'd like to welcome you personally to my dental practice, and I invite you to meet my highly experienced team of professionals.

"We have offered complete dental care of the highest quality since 1978. We provide Preventive Services, Tooth Whitening and Cosmetic Dentistry for a beautiful smile, Endodontics (root canal treatment) to treat painful teeth, Sedation Dentistry so you can relax, and Dental Implants to restore what is missing. We offer total care.

"Our approach to your health is simple: We use our education, experience and dedication to provide every patient with superior dental care.

"This passion for excellence is not just a goal, but a standard every member of our team holds.

"We also pride ourselves with our state of the art procedures, training and technology. This includes creating a beautiful smile using techniques that preserve as much of the original tooth as possible.

"Our abilities are renowned throughout the dental profession and I hope if you have any questions you will contact us by an e-mail note, by phone or just by dropping by."

Keep in mind the screen shape and dimensions. Your design needs to work in the normal screen proportions, regardless of how it looks when you post it here. Scrolling is OK, but the first impression needs to work.

Keep in mind that there will be about 250 words, or more, on each page.

Competitors web sites:

http://www.brevalkoortho.example/

http://www.quimbelfieldcare.example/

http://www.grinsatdoverellclinic.example/

http://www.trunwickfamilydentalcare.example/

http://www.morvanhaledental.example/

http://www.ubrigandental.example/

We need to compete with these.

Target Market(s)

Generally adults seeking the most experienced and comfortable-to-be-with dentist.

Industry/Entity Type

Training

Requirements
Must have
• Must stand apart from other dentists.
• Must be elegant.
• Must have a horizontal menu structure across all columns, NOT a vertical that requires scrolling, no popout, pop down, etc. menus.
• We are looking for something special.
• Do not waste your time or ours putting up templates and things you have used before.
• Personally, I do not see how someone outside the US can understand the northern California dental market. But you are welcome to try.
Should not have
• Flash or graphics that move
• The look of a template
• Folksy fonts
• Looks like you used it 20 times before

```html
<!DOCTYPE html>
<html lang="en">
<head>
<meta charset="utf-8">
<title>Calloway Dental</title>
<link rel="stylesheet" href="https://fonts.googleapis.com/css2?family=Fira+Sans:wght@400;500&display=swap">
<style>
  :root {
    --canvas: #ffffff;
    --page: #f5f5f5;
    --brand-red: #b4141b;
    --red-dark: #8e1015;
    --red-light: #d12027;
    --ink: #2f2f2f;
    --grey: #7a7a7a;
    --grey-light: #9a9a9a;
    --tab-bg: #f0eaea;
    --card-bg: #f7f7f7;
    --white: #ffffff;
  }
  * { box-sizing: border-box; margin: 0; padding: 0; }
  html, body { width: 1200px; height: 900px; overflow: hidden; background: var(--canvas); }
  body { font-family: "Fira Sans", "Trebuchet MS", sans-serif; color: var(--ink); position: relative; }

  .site { position: absolute; left: 90px; top: 135px; width: 1020px; height: 630px; background: var(--page); border-top: 5px solid var(--brand-red); }
  .abs { position: absolute; }

  /* header */
  .brand { left: 30px; top: 52px; display: flex; align-items: center; gap: 10px; }
  .brand-mark { width: 14px; height: 14px; background: var(--brand-red); border-radius: 50%; }
  .brand-name { font-size: 30px; font-weight: 500; color: var(--ink); letter-spacing: .2px; }

  .search { left: 753px; top: 43px; width: 146px; height: 20px; background: #f1e6e7; border: 1px solid #ddd; border-top-color: #c9c9c9; font-size: 11px; color: var(--grey-light); padding: 3px 8px; }
  .search svg { position: absolute; right: 5px; top: 3px; }
  .print { left: 916px; top: 46px; }
  .text-size { left: 950px; top: 46px; color: var(--grey); font-size: 11px; display: flex; align-items: baseline; gap: 3px; }
  .text-size span:nth-child(2) { font-size: 13px; }
  .text-size span:nth-child(3) { font-size: 16px; }

  /* navigation */
  .main-nav { left: 261px; top: 113px; display: flex; align-items: flex-end; gap: 4px; list-style: none; }
  .nav-item { height: 28px; min-width: 70px; text-align: center; padding: 0 8px; line-height: 29px; font-size: 14px; color: var(--ink); background: linear-gradient(#fbf7f7, var(--tab-bg)); border: 1px solid #e2dcdc; border-bottom: none; }
  .nav-item.is-active { height: 33px; line-height: 28px; margin-right: 2px; background: var(--brand-red); color: var(--white); font-weight: 500; border: none; }
  .nav-item.is-narrow { min-width: 61px; }

  /* hero */
  .hero { left: 30px; top: 146px; width: 960px; height: 272px; background: var(--red-dark); }
  .hero-photo { position: absolute; left: 0; top: 4px; width: 231px; height: 263px; background: linear-gradient(135deg, #e9e4de 0%, #d8b9a3 40%, #c79a84 65%, #ece8e4 100%); }
  .hero-panel { position: absolute; left: 231px; top: 0; width: 729px; height: 272px; background: linear-gradient(160deg, var(--red-dark) 0%, var(--brand-red) 55%, var(--red-light) 100%); color: var(--white); }
  .hero-title { position: absolute; font-size: 24px; font-weight: 400; }
  .intro-title { left: 20px; top: 22px; }
  .intro-text { position: absolute; left: 21px; top: 60px; width: 372px; font-size: 12px; line-height: 18px; }
  .news-title { left: 425px; top: 22px; }
  .news-list { position: absolute; left: 425px; top: 61px; width: 277px; }
  .news-item h3 { font-size: 13px; font-weight: 500; line-height: 18px; }
  .news-item p { font-size: 12px; line-height: 18px; }
  .news-item .read-more { display: block; text-align: right; color: var(--white); line-height: 18px; }
  .news-item + .news-item { margin-top: 4px; }

  .read-more { font-size: 12px; text-decoration: underline; color: var(--ink); }

  /* mission + features */
  .mission { left: 40px; top: 446px; width: 230px; font-size: 14px; line-height: 18px; color: var(--grey); }
  .feature { top: 400px; width: 220px; height: 120px; background: var(--card-bg); border-radius: 5px; box-shadow: 0 8px 16px rgba(0,0,0,.18); padding: 9px 13px; }
  .feature h2 { font-size: 18px; font-weight: 400; line-height: 22px; color: var(--ink); }
  .feature h2 em { font-style: normal; color: var(--brand-red); display: block; }
  .feature p { font-size: 12px; line-height: 15px; color: var(--grey); margin-top: 8px; }
  .feature .read-more { position: absolute; right: 17px; bottom: 7px; }
  .feature-quality { left: 280px; }
  .feature-care { left: 520px; }
  .feature-comfort { left: 761px; }

  /* footer */
  .footer { top: 578px; font-size: 10px; color: var(--grey); }
  .copyright { left: 40px; }
  .footer-nav { left: 267px; display: flex; gap: 23px; }
  .footer-nav a { color: var(--grey); text-decoration: underline; }
  .contact { left: 758px; display: flex; gap: 20px; align-items: center; }
</style>
</head>
<body>
<div class="site">
  <header>
    <div class="abs brand"><span class="brand-mark"></span><span class="brand-name">Calloway Dental</span></div>
    <div class="abs search">Search...
      <svg width="14" height="14" viewBox="0 0 14 14"><circle cx="5.5" cy="5.5" r="4" fill="none" stroke="#999" stroke-width="1.6"/><line x1="8.5" y1="8.5" x2="13" y2="13" stroke="#999" stroke-width="2"/></svg>
    </div>
    <svg class="abs print" width="18" height="16" viewBox="0 0 18 16"><rect x="4" y="1" width="10" height="5" fill="#ccc"/><rect x="1" y="6" width="16" height="7" rx="1" fill="#aaa"/><rect x="4" y="10" width="10" height="5" fill="#ddd"/></svg>
    <div class="abs text-size"><span>a</span><span>a</span><span>a</span></div>
    <ul class="abs main-nav">
      <li class="nav-item is-active">Home</li>
      <li class="nav-item is-narrow">Item 2</li>
      <li class="nav-item">Item 3</li>
      <li class="nav-item">Item 4</li>
      <li class="nav-item">item 5</li>
      <li class="nav-item">item 6</li>
      <li class="nav-item">item7</li>
      <li class="nav-item">item 8</li>
    </ul>
  </header>

  <section class="abs hero">
    <div class="hero-photo" role="img" aria-label="Photo of a patient receiving a dental check-up"></div>
    <div class="hero-panel">
      <h1 class="hero-title intro-title">Lorem ipsum dolar sit</h1>
      <p class="intro-text">Lorem ipsum dolor sit amet, consectetur adipiscing elit. Etiam consectetur velit in nisi sodales in pellentesque odio scelerisque. Vestibulum et velit id risus rutrum molestie. Phasellus vulputate est in tellus elementum eu vulputate neque tincidunt. Fusce et pretium urna. Morbi bibendum elementum ultrices. Curabitur porttitor laoreet nisi sed posuere. Suspendisse potenti. Curabitur porta varius tempus. Ut molestie mattis lacinia.<br>Vivamus convallis elit id ante mattis et semper mi cursus. Fusce gravida dapibus enim, nec egestas enim malesuada quis.</p>
      <h2 class="hero-title news-title">Latest news</h2>
      <div class="news-list">
        <article class="news-item">
          <h3>News item title 1</h3>
          <p>Lorem Ipsum is slechts een proeftekst uit het drukkerij- en zetterijwezen. Lorem Ipsum is de standaard proeftekst in deze bedrijfstak</p>
          <a class="read-more">read more</a>
        </article>
        <article class="news-item">
          <h3>Another news item title 2</h3>
          <p>Sinds de 16e eeuw, toen een onbekende drukker een zethaak met letters nam en ze door elkaar husselde om een font-catalogus te maken.</p>
          <a class="read-more">read more</a>
        </article>
      </div>
    </div>
  </section>

  <p class="abs mission">We use our education, experience and dedication to provide every patient with superior dental care</p>

  <article class="abs feature feature-quality">
    <h2>We provide <em>high quality</em></h2>
    <p>Lorem ipsum dolor sit amet, con sectetur adipiscing elit.</p>
    <a class="read-more">read more</a>
  </article>
  <article class="abs feature feature-care">
    <h2>State-of-the-art <em>dental care</em></h2>
    <p>Etiam consectetur velit in nisi soda les in pellentesque odio.</p>
    <a class="read-more">read more</a>
  </article>
  <article class="abs feature feature-comfort">
    <h2>Comfortable <em>caring environment</em></h2>
    <p>Etiam consectetur velit in nisi sodal in pellentesque odio scelerisque.</p>
    <a class="read-more">read more</a>
  </article>

  <footer>
    <p class="abs footer copyright">(c) Copyright 2010 Calloway Dental.</p>
    <nav class="abs footer footer-nav">
      <a>home</a><span>|</span><a>contact</a><span>|</span><a>privacy verklaring</a><span>|</span><a>sitemap</a>
    </nav>
    <div class="abs footer contact">
      <span><svg width="10" height="8" viewBox="0 0 10 8"><path d="M0 2 Q5 -1 10 2 L8 3 L7 2 L3 2 L2 3 Z M2 4 H8 V8 H2 Z" fill="#999"/></svg>&nbsp; 555 0142 886</span>
      <span>info@calloway.example</span>
    </div>
  </footer>
</div>
</body>
</html>
```